Letterhead Design for Law Firm

**Edit: I have added the photo of a bottom that I like.

------
We are looking for a re-design of our new letterhead. The letterhead is for a law firm and will be used for digital and traditionally printed correspondence.

Here are some suggestions:

- Please use colours are #8ec900 and simple black.
- Please do not use any type of "waves" at the bottom of the page. This is not in style at all.
- Please stay modern yet conservative.
- Please use font Segoe UI Light or similar if you can
- Avoid clipart or illustrations.
- Utilize ample white space in the layout so the design looks clean and information is easy to read at a glance. Don't overcrowd the letterhead.
- Make sure the letterhead design is consistent with our brand identity (see brambleford.ca)
-Please, no black headers or footers.

I am attaching my current letterhead and signature for your convenience.

Remember, the letterhead is an extension of our professional identity. We are a successful firm and trial lawyers who correspond with insurers, judges, lawyers, courts, clients, etc. Make it new, modern, attractive, yet powerful and conservative.

It needs to be easily printable. I would like the bleed removed in print so the black bar the bottom crosses the page (but the text is not near the edges)

Target Market(s)

Clients, Government Offices, Judiciary, Lawyers, Insurance Companies, Colleagues.

Industry/Entity Type

Law

Font styles to use
Other font styles liked:
• Segoe UI LIght, Calibri Light,

Colors
00AB8E
00BBA5
67D7C9
C6EFE9
E9F9F6

Requirements
Must have
• Everything that is on the letterhead now.
Nice to have
• Cutting Edge design, yet conservative.
Should not have
• law firm cliche design, images,

```html
<!DOCTYPE html>
<html lang="en">
<head>
<meta charset="utf-8">
<title>Hartwell Letterhead</title>
<link rel="stylesheet" href="https://fonts.googleapis.com/css2?family=Inter:wght@400;600;700&display=swap">
<style>
  :root {
    --backdrop: #e4e5e8;
    --paper: #ffffff;
    --band: #eceef1;
    --accent: #68c82e;
    --ink: #111111;
    --rule: #333333;
  }
  * { margin: 0; padding: 0; box-sizing: border-box; }
  html, body { width: 1200px; height: 1200px; overflow: hidden; background: var(--backdrop); }
  body { font-family: "Inter", Arial, sans-serif; color: var(--ink); }

  .letterhead {
    position: absolute; left: 152px; top: 20px;
    width: 896px; height: 1160px;
    background: var(--paper);
    overflow: hidden;
  }
  .header-band { position: absolute; left: 0; top: 0; width: 100%; height: 162px; background: var(--band); }
  .header-rule { position: absolute; left: 0; top: 162px; width: 100%; height: 3px; background: var(--accent); }

  .practice { position: absolute; top: 64px; font-size: 11px; line-height: 18.5px; text-transform: uppercase; }
  .practice--left { left: 78px; }
  .practice--right { left: 295px; }
  .practice__title { color: var(--accent); font-weight: 600; }
  .practice li { list-style: none; position: relative; padding-left: 13px; }
  .practice li::before {
    content: ""; position: absolute; left: 0; top: 7px;
    width: 4px; height: 4px; border-radius: 50%; background: var(--accent);
  }

  .brand { position: absolute; left: 603px; top: 66px; width: 214px; text-align: center; font-weight: 400; color: var(--ink); }
  .brand__name { font-size: 44px; line-height: 48px; letter-spacing: 1px; }
  .brand__tag { font-size: 11.5px; line-height: 16px; letter-spacing: 1.2px; text-transform: uppercase; }

  .body-text { position: absolute; left: 78px; font-size: 14px; line-height: 17px; }
  .strong { font-weight: 600; }

  .subject { position: absolute; left: 78px; top: 502px; width: 739px; font-size: 15.5px; line-height: 19px; font-weight: 600; }
  .subject__label { position: absolute; left: 5px; top: 0; }
  .subject__lines { margin-left: 68px; }
  .subject-rule { position: absolute; left: 78px; top: 569px; width: 739px; height: 2px; background: var(--rule); }

  .signature {
    position: absolute; left: 78px; top: 896px; width: 235px; height: 56px;
    background: linear-gradient(90deg, #f1f1f1, #e6e6e6);
  }

  .footer { position: absolute; top: 1090px; font-size: 12.5px; line-height: 16px; }
  .footer__label { font-weight: 600; display: inline-block; width: 70px; }
  .footer--clerk { left: 77px; }
  .footer--address { left: 312px; }
  .footer--phone { left: 529px; }
  .footer--web { left: 680px; letter-spacing: 1px; }
  .footer--web b { font-weight: 700; }
  .footer-divider { position: absolute; top: 1094px; width: 1px; height: 26px; background: var(--rule); }
</style>
</head>
<body>
<main class="letterhead">
  <div class="header-band"></div>
  <div class="header-rule"></div>

  <ul class="practice practice--left">
    <span class="practice__title">Practice Restricted:</span>
    <li>Serious Personal Injury</li>
    <li>Wrongful Death Litigation</li>
  </ul>
  <ul class="practice practice--right">
    <li>Employee Terminations</li>
    <li>Wrongful Dismissal Litigation</li>
    <li>Long-Term Disability Litigation</li>
  </ul>

  <div class="brand">
    <div class="brand__name">HARTWELL</div>
    <div class="brand__tag">Personal Injury Lawyers</div>
  </div>

  <p class="body-text strong" style="top:203px">Without Prejudice</p>
  <p class="body-text" style="top:238px">March 13, 2024</p>
  <p class="body-text strong" style="top:273px">By Email</p>
  <p class="body-text" style="top:307px">
    Norvale Insurance Company<br>
    Claims Litigation Department<br>
    240 Elmridge Road South<br>
    P.O. Box 3100<br>
    Kingsbury, ON &nbsp; N4K 2R7
  </p>
  <p class="body-text" style="top:410px">Attention: &nbsp;Mr. Dorian Pell</p>
  <p class="body-text" style="top:444px">Mr. Pell:</p>

  <div class="subject">
    <span class="subject__label">Re:</span>
    <div class="subject__lines">
      Marchetti v. Okafor et al.<br>
      DOL: &nbsp;September 12, 2019<br>
      Pre-Mediation Settlement Proposal – March 13th, 2024
    </div>
  </div>
  <div class="subject-rule"></div>

  <p class="body-text" style="top:858px">Yours very truly,</p>
  <p class="body-text strong" style="top:875px">HARTWELL PERSONAL INJURY LAWYERS</p>
  <div class="signature" role="img" aria-label="Handwritten signature of Owen R. Hartwell"></div>
  <p class="body-text strong" style="top:960px">Owen R. Hartwell</p>
  <p class="body-text" style="top:978px">Hartwell Law Professional Corporation</p>

  <div class="footer footer--clerk">
    <span class="footer__label">File Clerk:</span>Clara Whitcombe<br>
    <span class="footer__label">E-mail:</span>clara@brambleford.ca
  </div>
  <div class="footer-divider" style="left:290px"></div>
  <div class="footer footer--address">18 Alder Street W., Suite 902<br>Fernhill, ON &nbsp;L9T 3B5</div>
  <div class="footer-divider" style="left:506px"></div>
  <div class="footer footer--phone">T: 905-555-0142<br>F: 905-555-0177</div>
  <div class="footer-divider" style="left:655px"></div>
  <div class="footer footer--web">WWW.<b>BRAMBLEFORD</b>.CA</div>
</main>
</body>
</html>
```